Website Redesign using existing images, copy etc.

I'm looking for a website redesign/refresh of my current WordPress website. I would like to utilize the same photography, a new photo viewer, and an overall refresh of the entire design. This will need to be WordPress with simple accessibility to make changes as we add additional properties and make updates. We auction luxury real estate and luxury yachts for non-distressed sellers. It needs to be simple, luxurious and with ease of use for both web and especially mobile. www.HarborCrestBids.com

```html
<!DOCTYPE html>
<html lang="en">
<head>
<meta charset="utf-8">
<title>Harbor Crest — Real Estate &amp; Yachts</title>
<link href="https://fonts.googleapis.com/css2?family=Libre+Baskerville&family=Montserrat:wght@400;500;600&display=swap" rel="stylesheet">
<style>
:root{
  --gold:#9b8a66;
  --gold-dark:#877757;
  --card:#958667;
  --sand:#cbc2ac;
  --sand-light:#ddd6c6;
  --paper:#f1efeb;
  --ink:#2d2a26;
  --white:#ffffff;
  --serif:"Libre Baskerville", Georgia, serif;
  --sans:"Montserrat", Arial, sans-serif;
}
*{box-sizing:border-box;margin:0;padding:0}
html,body{width:1200px;height:3458px;overflow:hidden;background:var(--white);font-family:var(--sans);color:var(--ink)}
.page{position:relative;width:1200px;height:3458px}
.abs{position:absolute}
.mark{display:inline-block;border:2px solid currentColor;border-radius:50%}

/* hero */
.hero{left:0;top:0;width:1200px;height:580px;overflow:hidden}
.hero-photo{position:absolute;inset:0;background:linear-gradient(180deg,#3d3f49 0%,#5a5552 35%,#4b4a3c 65%,#3a3a2c 100%)}
.hero-curve{position:absolute;left:0;top:430px}
.nav-mark{left:88px;top:18px;width:46px;height:46px;color:#cfc6b4}
.nav{right:88px;top:36px;display:flex;gap:26px;font-size:13.5px;font-weight:500;color:#e9e4da;letter-spacing:.3px}
.nav .active{color:var(--sand);text-decoration:underline}
.nav .phone{display:flex;align-items:center;gap:6px}
.hero-title{left:0;width:1200px;top:182px;display:flex;justify-content:center;align-items:center;gap:22px;color:var(--white);font-family:var(--serif);font-size:44px;letter-spacing:18px}
.hero-title .mark{width:76px;height:76px;border-width:3px}
.hero-sub{left:0;width:1200px;top:276px;text-align:center;color:var(--white);font-size:16px;font-weight:500;letter-spacing:4px}
.btn{display:inline-flex;align-items:center;justify-content:center;border-radius:20px;font-size:12px;font-weight:600;letter-spacing:.6px;text-transform:uppercase}
.hero-btns{left:0;width:1200px;top:333px;display:flex;justify-content:center;gap:10px}
.hero-btns .btn{height:36px;padding:0 31px}
.btn-sand{background:var(--sand-light);color:var(--ink)}
.btn-gold{background:var(--gold);color:var(--white)}

/* intro */
.section-mark{width:38px;height:38px;color:var(--sand);left:581px}
.section-title{left:0;width:1200px;text-align:center;font-family:var(--serif);color:var(--gold);font-size:19px}
.intro-sub{left:0;width:1200px;top:734px;text-align:center;color:var(--gold);font-size:14px;font-weight:500}
.intro-text{left:170px;width:860px;top:772px;text-align:center;font-size:13.5px;line-height:24px}

/* press */
.press-band{left:0;top:935px;width:1200px;height:427px;background:var(--paper)}
.press-photo{left:652px;top:935px;width:548px;height:427px;background:linear-gradient(160deg,#c9a9a6 0%,#a98e8a 30%,#5d6a4a 70%,#3c4a30 100%)}
.press-logos{left:168px;top:980px;width:120px;display:flex;flex-direction:column;align-items:center;gap:26px}
.press-logos span{display:block;background:#8f8f8f;opacity:.55}
.press-card{left:361px;top:917px;width:291px;height:467px;background:var(--card);border-radius:10px;color:var(--white);text-align:center;padding:60px 30px 0}
.press-card .mark{width:36px;height:36px;color:var(--sand-light);opacity:.8}
.press-card h2{font-family:var(--serif);font-weight:400;font-size:19px;margin:18px 0 14px}
.press-card p{font-size:13px;line-height:22.4px}
.press-card .btn{margin-top:26px;height:34px;width:133px;background:var(--sand-light);color:var(--ink);text-transform:none;font-size:12.5px}

/* sold */
.slide{border:2px solid #ddd8cf;border-radius:8px;padding:2px}
.slide div{width:100%;height:100%;border-radius:6px}
.slide-side div{background:linear-gradient(160deg,#e6e3de,#cfcbc4)}
.slide-main div{background:linear-gradient(160deg,#c9a9a6 0%,#a58b88 30%,#5a6846 68%,#394730 100%)}
.caption{background:var(--white);border-radius:8px;box-shadow:0 4px 14px rgba(0,0,0,.08);text-align:center}
.caption h3{font-family:var(--serif);font-weight:400;color:var(--gold);font-size:17px}
.caption .btn{height:34px}
.dots{left:537px;top:2065px;display:flex;gap:6px}
.dots i{width:12px;height:12px;border:1px solid #a9a294;border-radius:50%}
.dots i.on{background:var(--gold);border-color:var(--gold)}
.sold-text{left:195px;width:810px;top:2110px;text-align:center;font-size:13.5px;line-height:20.8px}

/* upcoming */
.upcoming{left:0;top:2371px;width:1200px;height:820px;background:var(--paper)}
.up-photo{border:2px solid #d8d3c8;border-radius:8px;padding:2px}
.up-photo div{width:100%;height:100%;border-radius:6px}
.up-caption{width:401px;height:141px;padding-top:24px}
.up-caption p{font-family:var(--serif);font-size:12.5px;margin:6px 0 14px}
.btn-outline{border:1.5px solid #d4ccbb;color:var(--gold);background:var(--white);width:137px}
.btn-fill{background:var(--gold);color:var(--white);width:137px}
.view-all{left:535px;top:3000px;width:130px;height:36px;text-transform:none;font-size:12.5px}

/* footer */
.footer-shape{left:0;top:3110px}
.footer-logo{left:0;width:1200px;top:3203px;display:flex;justify-content:center;align-items:center;gap:18px;color:var(--white);font-family:var(--serif);font-size:30px;letter-spacing:13px}
.footer-logo .mark{width:54px;height:54px;border-width:2.5px}
.badge{left:122px;top:3268px;width:58px;height:58px;border-radius:50%;background:#ad9f83}
.badge-bar{left:122px;top:3333px;width:58px;height:12px;background:#ad9f83}
.foot-links{top:3295px;display:flex;flex-direction:column;gap:8px;font-size:14px;color:var(--white)}
.foot-links .active{color:var(--sand);text-decoration:underline}
.alerts{left:464px;top:3296px;font-size:14px;font-weight:600;color:var(--white);letter-spacing:.5px}
.field{height:38px;border:1.5px solid #c9bfa9;border-radius:20px;color:#e3dccd;font-size:14px;padding:0 22px;display:flex;align-items:center}
.submit{left:958px;top:3324px;width:118px;height:38px;background:var(--sand-light);color:var(--ink);text-transform:none;font-size:14px}
.copy-bar{left:0;top:3418px;width:1200px;height:40px;background:#f1efeb;display:flex;align-items:center;padding:0 88px;font-size:13.5px;color:#6d6658}
.copy-bar .legal{margin-left:12px;display:flex;gap:18px}
.copy-bar .social{margin-left:auto;display:flex;gap:13px}
.copy-bar .social i{width:20px;height:20px;border-radius:50%;background:#7c7566}
</style>
</head>
<body>
<div class="page">

  <header class="abs hero">
    <div class="hero-photo" role="img" aria-label="Dusk view of a Mediterranean-style estate with terraced gardens"></div>
    <svg class="hero-curve" width="1200" height="150" viewBox="0 0 1200 150" aria-hidden="true">
      <path d="M0 20 Q600 170 1200 0 L1200 150 L0 150Z" fill="var(--sand)"/>
      <path d="M0 80 Q600 200 1200 60 L1200 150 L0 150Z" fill="var(--white)"/>
    </svg>
  </header>

  <span class="abs mark nav-mark"></span>
  <nav class="abs nav">
    <span class="active">BUY</span><span>SELL</span><span>ABOUT</span><span>CONTACT</span>
    <span class="phone"><svg width="12" height="12" viewBox="0 0 24 24"><path d="M6.6 10.8a15 15 0 0 0 6.6 6.6l2.2-2.2a1 1 0 0 1 1-.25 11.4 11.4 0 0 0 3.6.57 1 1 0 0 1 1 1V20a1 1 0 0 1-1 1A17 17 0 0 1 3 4a1 1 0 0 1 1-1h3.5a1 1 0 0 1 1 1c0 1.25.2 2.45.57 3.57a1 1 0 0 1-.25 1z" fill="currentColor"/></svg>844-555-0187</span>
  </nav>

  <div class="abs hero-title"><span>HARBOR</span><span class="mark"></span><span>CREST</span></div>
  <div class="abs hero-sub">Real Estate &amp; Yachts</div>
  <div class="abs hero-btns">
    <span class="btn btn-sand">Browse Upcoming Auctions</span>
    <span class="btn btn-gold">Browse Past Successes</span>
  </div>

  <section>
    <span class="abs mark section-mark" style="top:659px"></span>
    <h1 class="abs section-title" style="top:708px;font-weight:400">Over One Billion Dollars of Auctions Marketed</h1>
    <div class="abs intro-sub">Real Estate &amp; Yachts</div>
    <p class="abs intro-text">The experience of hearing the auctioneer’s final proclamation of “SOLD!” is unparalleled. Whether it’s the initial meeting with the seller at their estate or yacht, or the triumphant raising of the paddle by the winning buyer, we relish every moment of the process and the ensuing festivities. We’re confident that you will, too.</p>
  </section>

  <section>
    <div class="abs press-band"></div>
    <div class="abs press-photo" role="img" aria-label="Aerial view of a waterfront villa with domed towers at sunset"></div>
    <div class="abs press-logos" aria-label="Press outlets">
      <span style="width:90px;height:52px"></span>
      <span style="width:108px;height:30px"></span>
      <span style="width:116px;height:26px"></span>
      <span style="width:92px;height:48px"></span>
      <span style="width:56px;height:52px"></span>
    </div>
    <div class="abs press-card">
      <span class="mark"></span>
      <h2>As Featured In</h2>
      <p>By offering top-tier properties and vessels globally, along with strategic auction dates, exceptional marketing tactics, and a diligent public relations team, even the most prominent media outlets have taken notice. Check out some of our latest press features.</p>
      <span class="btn">View Press</span>
    </div>
  </section>

  <section>
    <span class="abs mark section-mark" style="top:1472px"></span>
    <h2 class="abs section-title" style="top:1518px;font-weight:400">Sold by Harbor Crest</h2>
    <div class="abs slide slide-side" style="left:-20px;top:1563px;width:161px;height:425px"><div role="img" aria-label="Previous sold property, faded"></div></div>
    <div class="abs slide slide-main" style="left:159px;top:1563px;width:882px;height:425px"><div role="img" aria-label="Aerial view of a sold waterfront villa at sunset"></div></div>
    <div class="abs slide slide-side" style="left:1059px;top:1563px;width:161px;height:425px"><div role="img" aria-label="Next sold property, faded"></div></div>
    <div class="abs caption" style="left:447px;top:1938px;width:306px;height:102px;padding-top:22px">
      <h3>Frisco | Texas</h3>
      <span class="btn btn-sand" style="margin-top:14px;width:162px;background:var(--sand)">Success Story</span>
    </div>
    <div class="abs dots"><i></i><i></i><i></i><i></i><i></i><i class="on"></i><i></i></div>
    <p class="abs sold-text">Harbor Crest is a top-tier destination for luxury property auctions, having overseen the auction marketing of numerous high-end estates and yachts. Our team of luxury home auction experts is committed to helping property owners obtain the best value for their assets while ensuring a timely sale. Whether you have an expansive compound or a metropolitan penthouse, Harbor Crest has the necessary skills and expertise to facilitate various luxury real estate auctions. What’s even better? Our team takes care of every aspect of the process in cooperation with tour realtor/broker, including property tours, photography and cinematography, public relations and more. Apart from high-end real estate auctions, we can also organize and execute luxury yacht auctions to help boat owners find qualified buyers for their vessels. Interested in finding out more about our luxury home and yacht auctions? Explore our current listings and success stories!</p>
  </section>

  <section>
    <div class="abs upcoming"></div>
    <span class="abs mark section-mark" style="top:2450px"></span>
    <h2 class="abs section-title" style="top:2496px;font-weight:400">Upcoming Auctions</h2>

    <div class="abs up-photo" style="left:88px;top:2554px;width:500px;height:290px"><div role="img" aria-label="Aerial view of a yacht marina in a green island bay" style="background:linear-gradient(180deg,#9cc3e0 0%,#7a9a5a 40%,#2f6a8c 75%,#1e4e6e 100%)"></div></div>
    <div class="abs caption up-caption" style="left:137px;top:2811px">
      <h3>Cayon Bay Harbour, St. Kitts</h3>
      <p>Accepting Offers</p>
      <span class="btn btn-outline" style="height:31px">Learn More</span>
    </div>

    <div class="abs up-photo" style="left:612px;top:2554px;width:500px;height:290px"><div role="img" aria-label="Waterfront mansion with a docked yacht under blue sky" style="background:linear-gradient(180deg,#3f8fd6 0%,#8fc0ea 40%,#d9d9d4 62%,#3d6a44 85%,#2d4e5a 100%)"></div></div>
    <div class="abs caption up-caption" style="left:661px;top:2811px">
      <h3>Johns Creek, GA | Sold &amp; Closed</h3>
      <p>Auction Without Reserve</p>
      <span class="btn btn-fill" style="height:31px">Learn More</span>
    </div>

    <span class="abs btn btn-gold view-all">View All</span>
  </section>

  <footer>
    <svg class="abs footer-shape" width="1200" height="308" viewBox="0 0 1200 308" aria-hidden="true">
      <path d="M0 80 Q600 -40 1200 50 L1200 308 L0 308Z" fill="var(--sand)"/>
      <path d="M0 110 Q600 10 1200 90 L1200 308 L0 308Z" fill="var(--gold-dark)"/>
    </svg>
    <div class="abs footer-logo"><span>HARBOR</span><span class="mark"></span><span>CREST</span></div>
    <div class="abs badge" aria-label="Veteran-owned business badge"></div>
    <div class="abs badge-bar"></div>
    <div class="abs foot-links" style="left:253px"><span class="active">HOME</span><span>BUY</span><span>SELL</span></div>
    <div class="abs foot-links" style="left:336px"><span>ABOUT</span><span>BLOG</span><span>CONTACT</span></div>
    <div class="abs alerts">SIGN UP FOR HARBOR CREST ALERTS</div>
    <div class="abs field" style="left:465px;top:3324px;width:239px">Name</div>
    <div class="abs field" style="left:711px;top:3324px;width:239px">Email</div>
    <span class="abs btn submit">Submit</span>
    <div class="abs copy-bar">
      <span>© 2023 Harbor Crest. All Right Reserved &nbsp;&nbsp;|</span>
      <span class="legal"><span>Terms Of Service</span><span>Copyright Policy</span><span>Privacy Policy</span></span>
      <span class="social"><i></i><i></i><i></i><i></i></span>
    </div>
  </footer>

</div>
</body>
</html>
```